Design a Website Mockup for domain Tarvelmunkor.com

Design a website around [login to view URL] I want a website design that provides a simple, interactive game. No nudity.
Visitors, should they accept the challenge, put their sexuality detecting skills to the test. They will be presented with photos, and have to choose whether they are a female, or if they are infact a male in disguise. They will get a score, and then an option to share their score on social media sites. The actual structure of the game is up to you. Minimal design, with a non-instrusive space for advertising.

```html
<!DOCTYPE html>
<html lang="en">
<head>
<meta charset="utf-8">
<title>Tarvelmunkor.com</title>
<link rel="stylesheet" href="https://fonts.googleapis.com/css2?family=Arimo:wght@400&family=Oswald:wght@500;600&display=swap">
<style>
  :root {
    --frame: #2b2b2b;
    --bar-top: #f2f2f2;
    --bar-bottom: #c9c9c9;
    --page-light: #dadada;
    --page-dark: #6c6c6c;
    --panel: #d4d4d4;
    --band: #2a2a2a;
    --ink: #1f1f1f;
    --ink-soft: #333333;
    --white: #ffffff;
    --pink: #ef5aa8;
    --blue: #1f86cf;
    --green: #1fb51f;
    --share-box: #bcbcbc;
    --navy: #1d3a6b;
    --sky: #2b8fd8;
    --amber: #d9892a;
  }
  * { box-sizing: border-box; margin: 0; padding: 0; }
  html, body { width: 1200px; height: 900px; overflow: hidden; }
  body {
    position: relative;
    background: var(--frame);
    font-family: "Arimo", Arial, sans-serif;
    color: var(--ink);
  }
  .page {
    position: absolute; left: 16px; top: 0; width: 1168px; height: 900px;
    background: linear-gradient(135deg, var(--page-light) 0%, #c4c4c4 45%, var(--page-dark) 100%);
  }
  .column {
    position: absolute; left: 520px; top: 0; width: 163px; height: 820px;
    background: var(--frame);
  }
  .header {
    position: absolute; left: 19px; top: 0; width: 1164px; height: 83px;
    background: linear-gradient(var(--bar-top), var(--bar-bottom));
    border-radius: 0 0 10px 10px;
  }
  .brand {
    position: absolute; left: 28px; top: 6px;
    font-family: "Oswald", "Arial Narrow", sans-serif; font-weight: 600;
    font-size: 56px; line-height: 70px; letter-spacing: 1px;
    color: var(--ink-soft);
  }
  .brand small { font-size: 30px; letter-spacing: 0; }
  .play {
    position: absolute; left: 500px; top: -80px; width: 186px; height: 186px;
    border-radius: 50%; background: var(--frame);
    border: 7px solid #8a8a8a;
    display: flex; align-items: flex-end; justify-content: center;
    padding-bottom: 42px;
    font-family: "Oswald", "Arial Narrow", sans-serif; font-weight: 500;
    font-size: 38px; color: var(--white); text-decoration: none; letter-spacing: -0.5px;
  }
  .btn {
    position: absolute; top: 16px; width: 100px; height: 53px;
    border: 2px solid #9a9a9a; border-radius: 9px;
    background: linear-gradient(#fafafa, #cfcfcf);
    font-size: 27px; color: var(--ink-soft);
    display: flex; align-items: center; justify-content: center;
  }
  .btn.login { left: 697px; }
  .btn.signup { left: 865px; }
  .panel {
    position: absolute; left: 193px; top: 116px; width: 798px; height: 568px;
    background: var(--panel); border: 8px solid var(--frame); border-radius: 9px;
  }
  .welcome { position: absolute; left: 8px; top: 14px; font-size: 26px; color: var(--ink-soft); }
  .intro { position: absolute; left: 6px; top: 52px; width: 770px; font-size: 14.3px; line-height: 17px; }
  .choose { position: absolute; left: 0; top: 126px; width: 100%; text-align: center; font-size: 48px; }
  .mode {
    position: absolute; left: 0; width: 782px; background: var(--band);
    display: flex; align-items: center;
  }
  .mode h2 { font-weight: 400; font-size: 42px; padding-left: 10px; white-space: nowrap; }
  .mode p { color: var(--white); font-size: 12.3px; line-height: 15px; padding-left: 10px; padding-right: 10px; }
  .mode.trial { top: 196px; height: 64px; }
  .mode.trial h2 { color: var(--pink); }
  .mode.regular { top: 296px; height: 67px; }
  .mode.regular h2 { color: var(--blue); }
  .mode.practice { top: 387px; height: 65px; }
  .mode.practice h2 { color: var(--green); }
  .share {
    position: absolute; left: 6px; top: 467px; width: 770px; height: 72px;
    background: var(--share-box);
  }
  .share p { text-align: center; font-size: 14px; padding-top: 7px; color: var(--ink-soft); }
  .share a { position: absolute; top: 26px; font-size: 34px; text-decoration: none; }
  .share .friendbook { left: 36px; color: var(--navy); }
  .share .chirper { left: 316px; color: var(--sky); }
  .share .searchly { left: 588px; color: var(--amber); }
  .footer {
    position: absolute; left: 0; top: 816px; width: 1200px; height: 84px;
    background: linear-gradient(var(--bar-top), var(--bar-bottom));
    border-radius: 12px 12px 0 0;
    display: flex; align-items: center; justify-content: center;
    font-family: "Oswald", "Arial Narrow", sans-serif; font-weight: 500;
    font-size: 31px; color: var(--ink-soft);
  }
</style>
</head>
<body>
  <div class="page"></div>
  <div class="column"></div>

  <header class="header">
    <div class="brand">TARVELMUNKOR<small>.com</small></div>
    <div class="btn login">Login</div>
    <div class="btn signup">Sign up</div>
  </header>
  <a class="play" href="#">PLAY NOW</a>

  <main class="panel">
    <h1 class="welcome" style="font-weight:400">Welcome to Tarvelmunkor.com</h1>
    <p class="intro">Hello, put your sexuality detecting skills to the test. You will be presented with photos, and have to choose whether they are a female, or if they are infact a male in disguise. You will get a score, and then an option to share your score with your freinds and see who can score the most!</p>
    <div class="choose">Choose a game type!</div>

    <section class="mode trial">
      <h2>Time Trial</h2>
      <p>See how many you can get right within a certain time frame! points will be deducted when you guess wrong and highest score will be displayed on the leaderboards! will you be at the top?</p>
    </section>
    <section class="mode regular">
      <h2>Regular</h2>
      <p>Play the regualr version!, no time frame but you still get points deducted and will lose a life!<br>if you get all three of your lives lost you will lose! see if you can get the highest score and beat your friends!</p>
    </section>
    <section class="mode practice">
      <h2>Practice</h2>
      <p>Practice makes perfect!, In this mode there is no time nor is there any lives, here its all fun and games where you can test your perception to your hearts content! this is a great way to get to grips with the game if you are new!</p>
    </section>

    <div class="share">
      <p>Want to share your score instantly? Why not sign in using your Friendbook, Chirper or Searchly account?</p>
      <a class="friendbook" href="#">Friendbook</a>
      <a class="chirper" href="#">Chirper</a>
      <a class="searchly" href="#">Searchly</a>
    </div>
  </main>

  <footer class="footer">COPYRIGHT @ 2013</footer>
</body>
</html>
```